Bold and colurful E-liquid Design Template

I'm looking for a new label for my house range of vape e-liquids. I currently have almost 40 flavours, so I'm looking for a single label design that I can modify to create the rest of the flavours.
Each label will have the same design, but I'll change the color for each flavour and the name.
I'd like the label to be predominantly text based with bold text and bold colours. I like bold typographic styles. Also for each flavour I'd like to add 1 - 3 letters to represent the flavour. This can be in a larger font.
eg for
Blueberry I'll use the letter B
Pineapple Peach will use PP
Cinnamon Blueberry Muffin uses CBM
The colour used on the label will also be important so they stand out nicely on the shelf.
I've attached a psd mockup of the bottles I'll be using.

```html
<!DOCTYPE html>
<html lang="en">
<head>
<meta charset="utf-8">
<title>House Range E-Liquid Labels</title>
<link href="https://fonts.googleapis.com/css2?family=Archivo+Black&display=swap" rel="stylesheet">
<style>
  :root {
    --backdrop: #aeafb3;
    --panel: #ffffff;
    --ink-grey: #6b6c70;
    --blueberry: #1f9edc;
    --pineapple-peach: #f2a53a;
    --dark-roast: #9b1c5c;
  }
  html, body {
    margin: 0;
    width: 1084px;
    height: 1200px;
    overflow: hidden;
    background: var(--backdrop);
  }
  .canvas {
    position: relative;
    width: 1084px;
    height: 1200px;
  }
  .label {
    position: absolute;
    top: 165px;
    width: 300px;
    height: 870px;
  }
  .label--blueberry { left: 52px; --flavour: var(--blueberry); }
  .label--peach { left: 392px; --flavour: var(--pineapple-peach); }
  .label--roast { left: 732px; --flavour: var(--dark-roast); }
  .label svg { display: block; width: 300px; height: 870px; }
  .band { fill: var(--flavour); }
  .panel { fill: var(--panel); }
  .flavour-name, .range-name, .brand-name, .brand-tagline {
    fill: var(--flavour);
  }
  .strength, .volume { fill: var(--ink-grey); }
  .divider { stroke: var(--ink-grey); stroke-width: 2; }
  text {
    font-family: "Archivo Black", "Arial Black", sans-serif;
  }
</style>
</head>
<body>
<main class="canvas">

  <article class="label label--blueberry">
    <svg viewBox="0 0 300 870" aria-label="Blueberry e-liquid label">
      <rect class="band" x="0" y="0" width="300" height="870"/>
      <rect class="panel" x="0" y="88" width="300" height="688"/>
      <text class="flavour-name" font-size="68" transform="translate(52 768) rotate(-90)" textLength="677" lengthAdjust="spacingAndGlyphs">BLUEBERRY</text>
      <text class="range-name" font-size="52" transform="translate(97 460) rotate(-90)" textLength="367" lengthAdjust="spacingAndGlyphs">E-LIQUIDS</text>
      <text class="strength" font-size="195" x="245" y="236" textLength="47" lengthAdjust="spacingAndGlyphs">3</text>
      <text class="strength" font-size="54" x="243" y="298" textLength="48" lengthAdjust="spacingAndGlyphs">MG</text>
      <line class="divider" x1="215" y1="310" x2="292" y2="310"/>
      <text class="volume" font-size="104" x="204" y="404" textLength="89" lengthAdjust="spacingAndGlyphs">100</text>
      <text class="volume" font-size="50" x="251" y="460" textLength="41" lengthAdjust="spacingAndGlyphs">ML</text>
      <text class="brand-name" font-size="40" x="148" y="710" textLength="144" lengthAdjust="spacingAndGlyphs">HALDEN</text>
      <text class="brand-tagline" font-size="20" x="146" y="752" textLength="148" lengthAdjust="spacingAndGlyphs">PREMIUM E-LIQUID</text>
    </svg>
  </article>

  <article class="label label--peach">
    <svg viewBox="0 0 300 870" aria-label="Pineapple Peach e-liquid label">
      <rect class="band" x="0" y="0" width="300" height="870"/>
      <rect class="panel" x="0" y="88" width="300" height="688"/>
      <text class="flavour-name" font-size="56" transform="translate(42 766) rotate(-90)" textLength="675" lengthAdjust="spacingAndGlyphs">PINEAPPLE</text>
      <text class="flavour-name" font-size="100" transform="translate(118 523) rotate(-90)" textLength="432" lengthAdjust="spacingAndGlyphs">PEACH</text>
      <text class="range-name" font-size="52" transform="translate(172 460) rotate(-90)" textLength="367" lengthAdjust="spacingAndGlyphs">E-LIQUIDS</text>
      <text class="strength" font-size="195" x="245" y="236" textLength="47" lengthAdjust="spacingAndGlyphs">3</text>
      <text class="strength" font-size="54" x="243" y="298" textLength="48" lengthAdjust="spacingAndGlyphs">MG</text>
      <line class="divider" x1="215" y1="310" x2="292" y2="310"/>
      <text class="volume" font-size="104" x="204" y="404" textLength="89" lengthAdjust="spacingAndGlyphs">100</text>
      <text class="volume" font-size="50" x="251" y="460" textLength="41" lengthAdjust="spacingAndGlyphs">ML</text>
      <text class="brand-name" font-size="40" x="148" y="710" textLength="144" lengthAdjust="spacingAndGlyphs">HALDEN</text>
      <text class="brand-tagline" font-size="20" x="146" y="752" textLength="148" lengthAdjust="spacingAndGlyphs">PREMIUM E-LIQUID</text>
    </svg>
  </article>

  <article class="label label--roast">
    <svg viewBox="0 0 300 870" aria-label="Dark Roast Coffee e-liquid label">
      <rect class="band" x="0" y="0" width="300" height="870"/>
      <rect class="panel" x="0" y="88" width="300" height="688"/>
      <text class="flavour-name" font-size="155" transform="translate(114 771) rotate(-90)" textLength="680" lengthAdjust="spacingAndGlyphs">DRC</text>
      <text class="range-name" font-size="52" transform="translate(180 460) rotate(-90)" textLength="367" lengthAdjust="spacingAndGlyphs">E-LIQUIDS</text>
      <text class="strength" font-size="195" x="245" y="236" textLength="47" lengthAdjust="spacingAndGlyphs">3</text>
      <text class="strength" font-size="54" x="243" y="298" textLength="48" lengthAdjust="spacingAndGlyphs">MG</text>
      <line class="divider" x1="215" y1="310" x2="292" y2="310"/>
      <text class="volume" font-size="104" x="204" y="404" textLength="89" lengthAdjust="spacingAndGlyphs">100</text>
      <text class="volume" font-size="50" x="251" y="460" textLength="41" lengthAdjust="spacingAndGlyphs">ML</text>
      <text class="brand-name" font-size="40" x="148" y="710" textLength="144" lengthAdjust="spacingAndGlyphs">HALDEN</text>
      <text class="brand-tagline" font-size="20" x="146" y="752" textLength="148" lengthAdjust="spacingAndGlyphs">PREMIUM E-LIQUID</text>
    </svg>
  </article>

</main>
</body>
</html>
```